Varno Building Pty Ltd need an Identity!

We need a logo design for a building company based in Sydney, Australia. In addition - Business Card Layout. The colour scheme is to be black and red and communicate a professional yet 'hands on' approach to building.

Target Market(s)

Architects, Home Owners, Developers

Industry/Entity Type

Construction

Font styles to use
Serif
Sans Serif

Colors
ec1f27

Requirements
Must have
• Clear logo and professional direction.
Nice to have
• Use of initials as a possible logo
Should not have
• Graphics/pictures of houses, house roofs etc. Can be an abstracted form of a building.

```html
<!DOCTYPE html>
<html lang="en">
<head>
<meta charset="UTF-8">
<title>Varno Building Pty Ltd – Business Card</title>
<link href="https://fonts.googleapis.com/css2?family=Open+Sans:wght@400;700&display=swap" rel="stylesheet">
<style>
  :root {
    --red: #c4161c;
    --black: #111111;
    --ink: #2a2a2a;
    --paper: #ffffff;
    --backdrop: #c9c9cb;
  }
  * { margin: 0; padding: 0; box-sizing: border-box; }
  html, body {
    width: 1200px; height: 1200px; overflow: hidden;
    background: var(--backdrop);
    font-family: "Open Sans", Arial, sans-serif;
  }
  .card {
    position: absolute;
    left: 250px;
    width: 700px; height: 400px;
    background: var(--paper);
    box-shadow: 0 6px 18px rgba(0,0,0,0.18);
    overflow: hidden;
  }
  .card--front { top: 90px; }
  .card--back { top: 590px; }

  .wordmark {
    display: flex; align-items: center; gap: 14px;
    color: var(--black); font-weight: 700;
    white-space: nowrap;
  }
  .wordmark__square { background: var(--red); flex: none; }

  .card--front .wordmark {
    position: absolute; left: 50%; top: 50%;
    transform: translate(-50%, -50%);
    font-size: 36px; letter-spacing: 0.3px;
  }
  .card--front .wordmark__square { width: 42px; height: 42px; }

  .card--back .wordmark {
    position: absolute; left: 42px; top: 64px;
    font-size: 21px; gap: 10px;
  }
  .card--back .wordmark__square { width: 26px; height: 26px; }

  .holder {
    position: absolute; right: 52px; top: 52px; text-align: right;
    white-space: nowrap;
  }
  .holder__name { font-size: 30px; font-weight: 700; color: var(--black); line-height: 1.1; }
  .holder__role { font-size: 15px; color: var(--red); }
  .holder__tab {
    position: absolute; right: 0; top: 52px;
    width: 22px; height: 40px; background: var(--red);
  }

  .address {
    position: absolute; left: 110px; top: 218px;
    font-size: 16px; color: var(--ink); line-height: 1.35;
    white-space: nowrap;
  }
  .contact-list {
    position: absolute; left: 110px; top: 278px;
    list-style: none; font-size: 16px; color: var(--ink); line-height: 1.35;
    white-space: nowrap;
  }
  .contact-list li { display: flex; align-items: center; gap: 10px; }
  .contact-list svg { width: 14px; height: 14px; fill: var(--red); flex: none; }

  .card__bands { position: absolute; left: 0; bottom: 0; width: 700px; height: 34px; }
</style>
</head>
<body>

<section class="card card--front" aria-label="Card front">
  <div class="wordmark">
    <span class="wordmark__square"></span>
    <span class="wordmark__name">Varno Building Pty Ltd</span>
  </div>
</section>

<section class="card card--back" aria-label="Card back">
  <div class="wordmark">
    <span class="wordmark__square"></span>
    <span class="wordmark__name">Varno Building Pty Ltd</span>
  </div>

  <div class="holder">
    <div class="holder__name">Daniel Marsh</div>
    <div class="holder__role">President</div>
  </div>
  <span class="holder__tab"></span>

  <p class="address">14 Kellow Street, Marrick Park<br>PO Box 2150, Sydney NSW 2000</p>

  <ul class="contact-list">
    <li>
      <svg viewBox="0 0 16 16" aria-hidden="true"><path d="M3.5 1l2.5 3-1.5 2c.9 2 2.6 3.7 4.5 4.5l2-1.5 3 2.5-1.5 2.5C7 15 1 9 1 2.5z"/></svg>
      (02) 5550 1847
    </li>
    <li>
      <svg viewBox="0 0 16 16" aria-hidden="true"><path d="M1 3h14v10H1z M1 3l7 6 7-6" stroke="#fff" stroke-width="1.2"/></svg>
      info@varnobuilding.com
    </li>
    <li>
      <svg viewBox="0 0 16 16" aria-hidden="true"><circle cx="8" cy="8" r="7"/><path d="M1 8h14M8 1c3 3 3 11 0 14M8 1c-3 3-3 11 0 14" stroke="#fff" stroke-width="1" fill="none"/></svg>
      www.varnobuilding.com
    </li>
  </ul>

  <svg class="card__bands" viewBox="0 0 700 34" aria-hidden="true">
    <polygon points="0,22 430,22 422,34 0,34" fill="var(--black)"/>
    <polygon points="444,8 700,8 700,34 430,34" fill="var(--red)"/>
  </svg>
</section>

</body>
</html>
```